Geschäftspapiere für Rechnungen, Anschreiben etc.
Zielgruppe
Yogaunterricht - Einzelstunden, Workshops, Seminare etc.
Aufgabenstellung
Es soll weiche Übergänge haben mit dem bestehenden Logo und gerne den Farbverlauf nutzen. Auf das Briefpapier muss der Name, die Adresse, Web- und Emailadresse: www.velin-yoga.com

```html
<!DOCTYPE html>
<html lang="de">
<head>
<meta charset="utf-8">
<title>Velin Yoga – Briefpapier</title>
<link href="https://fonts.googleapis.com/css2?family=Arimo:wght@400;700&display=swap" rel="stylesheet">
<style>
  :root {
    --backdrop: #ecebe8;
    --paper: #ffffff;
    --ink: #111111;
    --muted: #8f8f8a;
    --rule: #cfcfcf;
    --brand-green: #3d5a33;
    --brand-green-dark: #2c3d2b;
    --brand-light: #a9cf9a;
    --footer-text: #ffffff;
    --footer-name: #c9d6c0;
  }
  * { box-sizing: border-box; margin: 0; padding: 0; }
  html, body {
    width: 1061px; height: 1200px; overflow: hidden;
    background: var(--backdrop);
    font-family: "Arimo", Arial, sans-serif;
  }
  .letterhead {
    position: absolute; left: 140px; top: 46px;
    width: 780px; height: 1108px;
    background: var(--paper);
    box-shadow: 0 4px 18px rgba(0,0,0,.12);
    overflow: hidden;
  }
  .brand {
    position: absolute; right: 62px; top: 36px;
    display: flex; flex-direction: column; align-items: center; gap: 10px;
  }
  .brand-mark {
    width: 58px; height: 58px; border-radius: 50%;
    border: 2px solid var(--brand-light);
  }
  .brand-name {
    font-size: 22px; letter-spacing: 2px; color: var(--muted);
    text-transform: uppercase;
  }
  .sender-line {
    position: absolute; left: 72px; top: 180px; width: 266px;
    font-size: 6.5px; color: var(--muted);
    padding-bottom: 4px; border-bottom: 1px solid var(--rule);
    white-space: nowrap;
  }
  .recipient {
    position: absolute; left: 72px; top: 228px;
    font-size: 11px; line-height: 13px; color: var(--ink);
  }
  .recipient .city { margin-top: 12px; }
  .subject {
    position: absolute; left: 86px; top: 340px;
    font-size: 15px; font-weight: 700; color: var(--muted);
  }
  .salutation {
    position: absolute; left: 86px; top: 398px;
    font-size: 13px; color: var(--ink);
  }
  .body-copy {
    position: absolute; left: 90px; top: 452px;
    font-size: 11px; line-height: 21.5px; color: var(--ink);
    list-style: none;
  }
  .fold-mark {
    position: absolute; left: 0; width: 22px; height: 1px; background: var(--rule);
  }
  .fold-mark.top { top: 362px; }
  .fold-mark.middle { top: 500px; }
  .fold-mark.bottom { top: 690px; }
  .footer-band {
    position: absolute; left: 0; right: 0; bottom: 0; height: 72px;
    background: linear-gradient(90deg, var(--brand-green-dark) 0%, var(--brand-green) 100%);
    color: var(--footer-text); font-size: 11px; line-height: 14px;
  }
  .footer-pattern {
    position: absolute; left: 0; top: 0; width: 230px; height: 72px;
    background: linear-gradient(90deg, #3a4a39 0%, var(--brand-green-dark) 100%);
  }
  .footer-address { position: absolute; left: 270px; top: 14px; }
  .footer-address .name { color: var(--footer-name); font-weight: 700; margin-bottom: 6px; }
  .footer-contact { position: absolute; left: 470px; top: 10px; }
  .contact-row { display: flex; align-items: flex-start; gap: 8px; margin-bottom: 6px; }
  .contact-row svg { flex: none; margin-top: 1px; }
  .icon-col { position: absolute; left: 252px; top: 36px; }
</style>
</head>
<body>
  <main class="letterhead">
    <div class="brand">
      <span class="brand-mark"></span>
      <span class="brand-name">Velin Yoga</span>
    </div>

    <p class="sender-line">Velin Yoga ◦ Mara Lindqvist ◦ Lindenallee 24 ◦ 35041 Weidental</p>

    <address class="recipient" style="font-style:normal">
      Frau<br>Vorname Nachname<br>Musterstrasse 9
      <div class="city">99999 Musterort</div>
    </address>

    <h1 class="subject">Hier steht der Betreff</h1>
    <p class="salutation">Sehr geehrte Frau Musterfrau,</p>

    <ul class="body-copy">
      <li>[Inhalt]</li><li>[Inhalt]</li><li>[Inhalt]</li><li>[Inhalt]</li>
      <li>[Inhalt]</li><li>[Inhalt]</li><li>[Inhalt]</li>
    </ul>

    <span class="fold-mark top"></span>
    <span class="fold-mark middle"></span>
    <span class="fold-mark bottom"></span>

    <footer class="footer-band">
      <div class="footer-pattern" role="img" aria-label="Dezentes ornamentales Muster in Dunkelgrün"></div>
      <svg class="icon-col" width="12" height="10" viewBox="0 0 12 10" aria-hidden="true">
        <rect x="0.5" y="0.5" width="11" height="9" fill="none" stroke="#fff"/>
        <path d="M0.5 0.5 L6 5.5 L11.5 0.5" fill="none" stroke="#fff"/>
      </svg>
      <div class="footer-address">
        <div class="name">Mara Lindqvist-Berg</div>
        <div>Lindenallee 24</div>
        <div>35041 Weidental</div>
      </div>
      <div class="footer-contact">
        <div class="contact-row">
          <svg width="12" height="12" viewBox="0 0 24 24" aria-hidden="true"><path fill="#fff" d="M6.6 10.8a15 15 0 0 0 6.6 6.6l2.2-2.2a1 1 0 0 1 1-.25 11.4 11.4 0 0 0 3.6.57 1 1 0 0 1 1 1V20a1 1 0 0 1-1 1A17 17 0 0 1 3 4a1 1 0 0 1 1-1h3.5a1 1 0 0 1 1 1c0 1.25.2 2.45.57 3.57a1 1 0 0 1-.25 1z"/></svg>
          <span>Tel.: 0170/5521934</span>
        </div>
        <div class="contact-row">
          <svg width="12" height="12" viewBox="0 0 24 24" aria-hidden="true"><circle cx="12" cy="12" r="4" fill="none" stroke="#fff" stroke-width="3"/><path d="M16 8v6a3 3 0 0 0 6 0v-2a10 10 0 1 0-4 8" fill="none" stroke="#fff" stroke-width="3"/></svg>
          <span>mail@velin-yoga.com<br>www.velin-yoga.com</span>
        </div>
      </div>
    </footer>
  </main>
</body>
</html>
```